Business Card template designs

We need a lot of Business card designs.
Your designs will get exposure on our newly opened business-card printing website.
We are committed to quality of paper and packages we use, so they will come up very fancy.

Here is your advantage. We will put the profile of the graphic designer on our site so that you can showcase your designs to people around the world and in Japan.

A profile is not mandatory, although we encourage graphic designers to have a profile to get continuous work in the future.
We are looking forward to having many good designs.

The right of the use of design will be owned by us.
The design may be used to the products other than
business cards.

Target Market(s)

designer,photographer,creator,artist

Industry/Entity Type

Printing

Contact Information for Business Card

The back design is important.
Please check the reference file.

Requirements
Must have
• Please include the following, required information on your business card designs.
• Name: Haruna Okabe
• Title: Designer
• Web: https://www.ketori.co.jp/kt/
• Address: 4-17 Kamiharuta-Cho Meguro-ku, Tokyo
• Email: info@kketori.com
• Phone: 03 4816 3907
• Mobile: 070 2143 6658
• * For Japanese sites, we will convert the text portion to Japanese characters.
• * In case of 28mmx70mm only include Name,Enail,Phone and SNS account(https://www.facebook.com/kketori.com)
• 1. colorful
• 2. simple
• 3. natural
• 4. modern
• 5. cool
• 6. sporty
• Please make variations of the same image with 3-6
• different colors / patterns for one design so that
• customers can compare and choose.
• If you want to use a same picture, please make make
• copies and paste on each different types of design.
Nice to have
• You may also use, the following non-required information.
• Company Name: Ketori, Inc.
• Fax: 03-4173-9620
• Open space for company logo

```html
<!DOCTYPE html>
<html lang="en">
<head>
<meta charset="utf-8">
<title>Ketori business card – front and back</title>
<link rel="stylesheet" href="https://fonts.googleapis.com/css2?family=Arimo:wght@400;700&display=swap">
<style>
  :root {
    --backdrop: #a4a5a5;
    --brand-blue: #0b2b7c;
    --paper: #e9eaed;
    --ink: #1f2124;
    --light-text: #dfe3ee;
  }
  * { box-sizing: border-box; margin: 0; padding: 0; }
  html, body {
    width: 1105px;
    height: 1200px;
    overflow: hidden;
    background: var(--backdrop);
    font-family: "Arimo", Arial, sans-serif;
  }
  .canvas { position: relative; width: 1105px; height: 1200px; }
  .card {
    position: absolute;
    left: 182px;
    width: 747px;
    height: 427px;
    background: var(--brand-blue);
    overflow: hidden;
  }
  .card--front { top: 119px; }
  .card--back { top: 635px; }

  .front__panel { position: absolute; inset: 0; }

  .wordmark {
    position: absolute;
    color: var(--paper);
    font-weight: 400;
    letter-spacing: 2px;
    line-height: 1;
  }
  .card--front .wordmark { left: 56px; top: 75px; font-size: 72px; }
  .card--back .wordmark {
    left: 0; right: 0; top: 162px;
    text-align: center; font-size: 88px;
  }

  .contact {
    position: absolute;
    right: 14px;
    top: 162px;
    text-align: right;
    color: var(--ink);
  }
  .contact__name { font-size: 24px; line-height: 30px; padding-right: 2px; }
  .contact__title { font-size: 19px; line-height: 24px; padding-right: 2px; margin-bottom: 14px; }
  .contact__list { list-style: none; }
  .contact__item {
    display: flex;
    justify-content: flex-end;
    align-items: center;
    gap: 8px;
    font-size: 17.5px;
    line-height: 29px;
  }
  .contact__icon { width: 20px; height: 20px; fill: var(--ink); flex: none; }

  .company {
    position: absolute;
    right: 14px;
    bottom: 14px;
    font-size: 17px;
    color: var(--ink);
  }
  .company__name { font-weight: 700; }

  .back__web {
    position: absolute;
    left: 0; right: 0; top: 364px;
    text-align: center;
    font-size: 17px;
    color: var(--light-text);
  }
</style>
</head>
<body>
<main class="canvas">

  <section class="card card--front" aria-label="Business card front">
    <svg class="front__panel" viewBox="0 0 747 427" width="747" height="427" aria-hidden="true">
      <path fill="var(--paper)" d="M197 427 L592 116 C626 86 640 50 680 46 C716 43 734 72 747 96 L747 427 Z"/>
    </svg>

    <p class="wordmark">Ketori</p>

    <div class="contact">
      <h1 class="contact__name">Haruna Okabe</h1>
      <p class="contact__title">Designer</p>
      <ul class="contact__list">
        <li class="contact__item">03 4816 3907
          <svg class="contact__icon" viewBox="0 0 20 20" aria-label="Phone"><path d="M2 7c0-3 3-4 8-4s8 1 8 4v1h-4V6.5c-1-.6-7-.6-8 0V8H2z"/><path d="M5 10l2-3h6l2 3v6H5z"/><circle cx="10" cy="12.5" r="1.8" fill="var(--paper)"/></svg>
        </li>
        <li class="contact__item">070 2143 6658
          <svg class="contact__icon" viewBox="0 0 20 20" aria-label="Mobile"><path d="M6 1h8a1.5 1.5 0 0 1 1.5 1.5v15A1.5 1.5 0 0 1 14 19H6a1.5 1.5 0 0 1-1.5-1.5v-15A1.5 1.5 0 0 1 6 1zm.5 2.5v11h7v-11z"/></svg>
        </li>
        <li class="contact__item">03-4173-9620
          <svg class="contact__icon" viewBox="0 0 20 20" aria-label="Fax"><path d="M5 3h9v5H5z"/><path d="M2 9h16v8H2zm3 4v1h10v-1z" fill-rule="evenodd"/></svg>
        </li>
        <li class="contact__item">info@kketori.com
          <svg class="contact__icon" viewBox="0 0 20 20" aria-label="Email"><path d="M2 5h16v1.5l-8 5-8-5z"/><path d="M2 8.3l8 5 8-5V15H2z"/></svg>
        </li>
        <li class="contact__item">www.ketori.co.jp/kt/
          <svg class="contact__icon" viewBox="0 0 20 20" aria-label="Website"><circle cx="10" cy="10" r="8"/><path d="M6 6c2 0 3 1 2 3s-3 1-3 3 2 2 2 4M13 4c-1 2 1 3 3 3M12 12c1 1 3 1 3 3" stroke="var(--paper)" stroke-width="1.4" fill="none"/></svg>
        </li>
      </ul>
    </div>

    <p class="company"><span class="company__name">Ketori, Inc.</span>4-17 Kamiharuta-Cho,Meguro-ku,Tokyo</p>
  </section>

  <section class="card card--back" aria-label="Business card back">
    <p class="wordmark">Ketori</p>
    <p class="back__web">www.ketori.co.jp/kt</p>
  </section>

</main>
</body>
</html>
```